Website Design for Nuvexa Cloud As a Service

We are building a service to allow customers to own their own private clouds easily and cheaply. Owning your own private cloud saves costs, and offers more flexibility than a public cloud provider but has historically been a complex and expensive option.

We plan to offer a service where we build and maintain your own private cloud on your own hardware for a cheap monthly costs. Similar to this service - https://nimbarvo.com/solutions/private-cloud

We already have a logo and branding in place - we'd like a website design to be tailored from this branding, see attached logo design.

Feel free to add important elements on the home page such as testimonials, client/partner logos, contact form, social media, etc using placeholder contents in addition to the document we attached.

We also plan to add sub-pages in the future so please make sure that your website design has a full navigation menu.

An example of the site we like: https://www.vosketri.com/ we'd be happy for you to take inspiration from this website.

Target Market(s)

B2B focused, we are targeting start-up/small/medium sized companies who needs help with their cloud and IT infrastructure.

Industry/Entity Type

IT

Number of Pages Required

1 page

Font styles to use
Other font styles liked:
• Please refer to the attachment - font must have Mayeka Demi Bold & Retroica

Requirements
Must have
• Please add placeholder menu since we're planning to have subpages later on.

```html
<!DOCTYPE html>
<html lang="en">
<head>
<meta charset="utf-8">
<title>Nuvexa Cloud as a Service</title>
<link rel="stylesheet" href="https://fonts.googleapis.com/css2?family=Lexend:wght@500;600;700&family=Lato:wght@400;700&display=swap">
<style>
:root{
  --navy:#0b2d63;
  --navy-deep:#061a3d;
  --blue:#1a8ed8;
  --cyan:#1fd0e6;
  --ink:#111;
  --text:#444;
  --grey-band:#f2f2f2;
  --pale-blue:#e6f1f9;
  --white:#fff;
  --footer:#000;
}
*{margin:0;padding:0;box-sizing:border-box}
html,body{width:1200px;height:3527px;overflow:hidden}
body{position:relative;font-family:"Lato",sans-serif;color:var(--text);background:var(--white)}
.abs{position:absolute}
.head{font-family:"Lexend",sans-serif;font-weight:600;color:var(--ink)}
.btn{position:absolute;display:flex;align-items:center;justify-content:center;border-radius:28px;font-family:"Lexend",sans-serif;font-weight:600;font-size:14px;color:var(--white);background:linear-gradient(90deg,var(--blue),var(--cyan))}
.brand{display:flex;align-items:center;gap:8px;font-family:"Lexend",sans-serif;font-weight:600;color:var(--white);white-space:nowrap}
.brand-dot{width:30px;height:30px;border-radius:50%;background:var(--blue)}

/* hero */
.hero{left:0;top:0;width:1200px;height:685px;background:radial-gradient(circle at 78% 35%,#1b5fae 0%,var(--navy) 45%,var(--navy-deep) 100%)}
.hero-art{left:620px;top:80px;width:560px;height:470px;border-radius:20px;background:radial-gradient(ellipse at 50% 50%,rgba(31,208,230,.45),rgba(26,142,216,.15) 60%,transparent 75%)}
.nav a{color:var(--white);text-decoration:none;position:absolute;white-space:nowrap;font-size:15px}
.login{left:960px;top:25px;width:128px;height:39px;font-size:15px;gap:8px}
.hero-title{left:111px;top:160px;width:640px;font-size:41px;line-height:50px;color:var(--white);font-weight:700;white-space:nowrap}
.hero-copy{left:111px;top:369px;width:600px;font-size:12.5px;line-height:26px;color:var(--white);white-space:nowrap}
.hero-btn{left:112px;top:463px;width:154px;height:56px;font-size:15px}

/* benefits */
.benefit-cloud{left:144px;top:790px;width:405px;height:295px;border-radius:150px;background:var(--pale-blue)}
.benefit-icon{left:112px;top:905px;width:88px;height:62px;border-radius:31px;background:linear-gradient(90deg,var(--blue),#3aa6e8)}
.benefit-title{left:219px;top:905px;font-size:33px;line-height:40px;color:#7a7a7a;font-weight:600;white-space:nowrap}
.benefit-title span{color:var(--blue)}
.benefit-rule{left:597px;top:822px;width:2px;height:233px;background:var(--blue)}
.ticks{left:619px;top:788px;width:500px;list-style:none}
.ticks li{position:absolute;left:0;width:500px;padding-left:25px;font-size:14px;line-height:20px;color:var(--text);white-space:nowrap}
.tick{position:absolute;left:0;top:3px;width:14px;height:14px}

/* transformation */
.band{left:0;top:1189px;width:1200px;height:708px;background:var(--grey-band)}
.band-title{left:0;top:1251px;width:1200px;text-align:center;font-size:33px}
.band-rule{left:566px;top:1309px;width:68px;height:4px;background:var(--blue);border-radius:2px}
.band-copy{left:100px;top:1330px;width:1000px;text-align:center;font-size:12.5px;line-height:26px;color:var(--ink);white-space:nowrap}
.card{position:absolute;top:1429px;width:231px;height:267px;background:var(--white);border-radius:6px;overflow:hidden}
.card.tall{height:300px}
.card-shade{position:absolute;right:-20px;top:-10px;width:140px;height:110px;border-radius:60px;background:var(--pale-blue)}
.card-icon{position:absolute;left:14px;top:16px;width:50px;height:50px;border-radius:50%;background:linear-gradient(135deg,#bde0f6,var(--pale-blue))}
.card-icon svg{position:absolute;left:8px;top:8px}
.card h3{position:absolute;left:21px;top:76px;font-size:22px;color:var(--ink)}
.card p{position:absolute;left:21px;top:113px;width:215px;font-size:13.5px;line-height:25.6px;color:var(--text);white-space:nowrap}
.card a{position:absolute;left:21px;font-family:"Lexend",sans-serif;font-weight:600;font-size:14px;color:var(--blue);text-decoration:underline}
.start-btn{left:492px;top:1771px;width:152px;height:54px}

/* public cloud */
.public{left:0;top:1897px;width:1200px;height:592px;background:linear-gradient(100deg,#1a8fb8 0%,#17b6cf 45%,#22d2e4 100%)}
.public-title{left:249px;top:1965px;font-size:31px;color:var(--white);white-space:nowrap}
.public-rule{left:272px;top:2055px;width:3px;height:185px;background:var(--white)}
.public-copy{left:295px;width:700px;font-size:14.5px;line-height:26px;color:var(--white);white-space:nowrap}
.talk-btn{left:292px;top:2360px;width:141px;height:55px;background:var(--white);color:var(--blue)}

/* difference */
.diff-title{left:112px;top:2590px;font-size:33px;white-space:nowrap}
.diff-title span{color:var(--blue)}
.diff-list li{position:absolute;left:112px;width:480px;padding-left:31px;font-size:14.5px;line-height:26px;color:var(--text);list-style:none;white-space:nowrap}
.diff-list .tick{top:6px;width:16px;height:16px}
.diff-btn{left:111px;top:2966px;width:153px;height:53px;font-size:15px}
.diff-back{left:664px;top:2573px;width:424px;height:446px;background:linear-gradient(160deg,var(--cyan),var(--blue))}
.diff-photo{left:603px;top:2617px;width:438px;height:359px;border-radius:4px;background:radial-gradient(circle at 50% 40%,#1f7ed0 0%,#102c5c 55%,#2a1a20 100%)}

/* footer */
.footer{left:0;top:3113px;width:1200px;height:414px;background:var(--footer)}
.email{left:111px;top:3254px;width:274px;height:39px;border-radius:20px;background:var(--white);padding-left:20px;display:flex;align-items:center;font-size:14px;color:#888}
.email-send{position:absolute;right:4px;top:4px;width:31px;height:31px;border-radius:50%;background:var(--blue)}
.social{left:111px;top:3317px;display:flex;gap:6px}
.social span{width:33px;height:33px;border-radius:50%;border:2px solid var(--white);display:block}
.fcol h4{position:absolute;top:3180px;font-family:"Lexend",sans-serif;font-weight:600;font-size:18px;color:var(--white);white-space:nowrap}
.fcol a,.fcol div{position:absolute;font-size:14.5px;color:var(--white);text-decoration:none;white-space:nowrap}
.contact-ico{position:absolute;width:14px;height:14px}
.f-rule{left:111px;top:3425px;width:978px;height:1px;background:#2a2a2a}
.copyright{left:0;top:3462px;width:1200px;text-align:center;font-size:14.5px;color:var(--white)}
</style>
</head>
<body>

<!-- hero -->
<section>
  <div class="hero abs"></div>
  <div class="hero-art abs" role="img" aria-label="Glowing cloud above a laptop showing data dashboards"></div>
  <div class="brand abs" style="left:111px;top:12px;font-size:29px"><span class="brand-dot"></span>Nuvexa Cloud</div>
  <nav class="nav">
    <a style="left:482px;top:36px">Home</a>
    <a style="left:578px;top:36px">About</a>
    <a style="left:678px;top:36px">Product</a>
    <a style="left:790px;top:36px">Solutions</a>
  </nav>
  <div class="btn login"><svg width="13" height="14" viewBox="0 0 13 14"><circle cx="6.5" cy="4" r="3.5" fill="#fff"/><path d="M0 14c0-4 3-6 6.5-6s6.5 2 6.5 6z" fill="#fff"/></svg>Login</div>
  <h1 class="hero-title head abs">A groundbreaking way<br>for your small business to<br>benefit from the power<br>of the cloud</h1>
  <p class="hero-copy abs">Nuvexa Cloud as a Service is here to help small businesses utilise the power of the<br>cloud without complicated set-ups or scary price tags. Ready to modernise your<br>infrastructure with a fully managed private cloud solution from NCaaS?</p>
  <div class="btn hero-btn">Contact Us</div>
</section>

<!-- benefits -->
<section>
  <div class="benefit-cloud abs" role="img" aria-label="Large faint cloud decoration"></div>
  <div class="benefit-icon abs" role="img" aria-label="Small blue cloud icon"></div>
  <h2 class="benefit-title head abs">How <span>NCAAS benefits</span><br>your business</h2>
  <div class="benefit-rule abs"></div>
  <ul class="ticks abs">
    <li style="top:0"><svg class="tick" viewBox="0 0 14 14"><circle cx="7" cy="7" r="7" fill="#1a8ed8"/><path d="M4 7.2l2 2 4-4" stroke="#fff" stroke-width="1.6" fill="none"/></svg>Totally flexible – get the cloud you want and the latest<br>innovations you need</li>
    <li style="top:59px"><svg class="tick" viewBox="0 0 14 14"><circle cx="7" cy="7" r="7" fill="#1a8ed8"/><path d="M4 7.2l2 2 4-4" stroke="#fff" stroke-width="1.6" fill="none"/></svg>Faster – our private cloud solutions outpace public clouds</li>
    <li style="top:98px"><svg class="tick" viewBox="0 0 14 14"><circle cx="7" cy="7" r="7" fill="#1a8ed8"/><path d="M4 7.2l2 2 4-4" stroke="#fff" stroke-width="1.6" fill="none"/></svg>Greater value for money – totally transparent pricing for no nasty<br>month-end surprises</li>
    <li style="top:157px"><svg class="tick" viewBox="0 0 14 14"><circle cx="7" cy="7" r="7" fill="#1a8ed8"/><path d="M4 7.2l2 2 4-4" stroke="#fff" stroke-width="1.6" fill="none"/></svg>No consultancy fees – we’ll work with you and charge set fees for<br>everything</li>
    <li style="top:216px"><svg class="tick" viewBox="0 0 14 14"><circle cx="7" cy="7" r="7" fill="#1a8ed8"/><path d="M4 7.2l2 2 4-4" stroke="#fff" stroke-width="1.6" fill="none"/></svg>Management, monitoring and maintenance – they’re all included<br>in your monthly price</li>
    <li style="top:275px"><svg class="tick" viewBox="0 0 14 14"><circle cx="7" cy="7" r="7" fill="#1a8ed8"/><path d="M4 7.2l2 2 4-4" stroke="#fff" stroke-width="1.6" fill="none"/></svg>Tried and tested cloud solutions – we’ll deploy the right<br>Terrastack solutions for your business</li>
  </ul>
</section>

<!-- transformation -->
<section>
  <div class="band abs"></div>
  <h2 class="band-title head abs">NCAAS can drive your digital transformation today</h2>
  <div class="band-rule abs"></div>
  <p class="band-copy abs">NCAAS is here to help you switch on your cloud transformation in a way that works best for you. &nbsp;We deliver and support fully<br>managed private cloud solutions that are:</p>

  <div class="card" style="left:112px">
    <div class="card-icon"><svg width="34" height="34" viewBox="0 0 34 34"><circle cx="20" cy="17" r="11" fill="none" stroke="#1a8ed8" stroke-width="2"/><path d="M20 17l4-5M2 13h10M4 18h8M6 23h8" stroke="#1a8ed8" stroke-width="2"/></svg></div>
    <h3 class="head">Fast</h3>
    <p>Lorem ipsum dolor sit amet,<br>consectetur adipiscing elit,<br>sed do eiusmod tempor<br>incididunt ut labore et</p>
    <a style="top:237px">Learn More</a>
  </div>
  <div class="card tall" style="left:360px">
    <div class="card-shade"></div>
    <div class="card-icon"><svg width="34" height="34" viewBox="0 0 34 34"><circle cx="15" cy="12" r="9" fill="none" stroke="#1a8ed8" stroke-width="2"/><rect x="10" y="22" width="22" height="10" fill="none" stroke="#1a8ed8" stroke-width="2"/></svg></div>
    <h3 class="head">Easy</h3>
    <p>Lorem ipsum dolor sit amet,<br>consectetur adipiscing elit,<br>sed do eiusmod tempor<br>incididunt ut labore et<br>dolore magna</p>
    <a style="top:264px">Learn More</a>
  </div>
  <div class="card" style="left:610px">
    <div class="card-icon"><svg width="34" height="34" viewBox="0 0 34 34"><path d="M19 3l-7 15h7l-4 13 11-17h-7l4-11z" fill="none" stroke="#1a8ed8" stroke-width="2"/></svg></div>
    <h3 class="head">Powerful</h3>
    <p>Lorem ipsum dolor sit amet,<br>consectetur adipiscing elit,<br>sed do eiusmod tempor<br>incididunt ut labore et</p>
    <a style="top:237px">Learn More</a>
  </div>
  <div class="card" style="left:859px">
    <div class="card-icon"><svg width="34" height="34" viewBox="0 0 34 34"><path d="M4 30h26M10 30V18h6v12M20 14h8M24 4v26" stroke="#1a8ed8" stroke-width="2" fill="none"/></svg></div>
    <h3 class="head">Scalable</h3>
    <p>Lorem ipsum dolor sit amet,<br>consectetur adipiscing elit,<br>sed do eiusmod tempor<br>incididunt ut labore et</p>
    <a style="top:237px">Learn More</a>
  </div>
  <div class="btn start-btn">Get Started</div>
</section>

<!-- public cloud -->
<section>
  <div class="public abs" role="img" aria-label="Teal-tinted photo of a developer working at a laptop"></div>
  <h2 class="public-title head abs">If you’re using a public cloud now…</h2>
  <div class="public-rule abs"></div>
  <p class="public-copy abs" style="top:2046px">You could be paying too much… Public cloud pricing structures have a habit of sneakily scaling<br>up very quickly. With NCAAS, you’ll always know what you’re paying for your private cloud<br>services.</p>
  <p class="public-copy abs" style="top:2149px">You’re likely not getting the benefits of full functionality… Public cloud providers cannot adopt<br>new innovations and functions as quickly and easily as the private cloud solutions you’ll get<br>from NCAAS.</p>
  <p class="public-copy abs" style="top:2252px">You’ll be tied to the services your provider can provide… Public cloud providers will have a<br>limited suite of products and services to offer you. A NCAAS private cloud has no such<br>limitations</p>
  <div class="btn talk-btn">Let’s talk</div>
</section>

<!-- difference -->
<section>
  <h2 class="diff-title head abs">The <span>NCAAS</span> Difference</h2>
  <ul class="diff-list">
    <li style="top:2658px"><svg class="tick" viewBox="0 0 14 14"><circle cx="7" cy="7" r="7" fill="#1a8ed8"/><path d="M4 7.2l2 2 4-4" stroke="#fff" stroke-width="1.6" fill="none"/></svg>We’ll quickly get to grips with what your organisation needs,<br>and deliver it via our private cloud solutions.</li>
    <li style="top:2735px"><svg class="tick" viewBox="0 0 14 14"><circle cx="7" cy="7" r="7" fill="#1a8ed8"/><path d="M4 7.2l2 2 4-4" stroke="#fff" stroke-width="1.6" fill="none"/></svg>Enjoy the ease of the public cloud, combined with the<br>features, innovations and flexibility of the private cloud.</li>
    <li style="top:2812px"><svg class="tick" viewBox="0 0 14 14"><circle cx="7" cy="7" r="7" fill="#1a8ed8"/><path d="M4 7.2l2 2 4-4" stroke="#fff" stroke-width="1.6" fill="none"/></svg>You can focus on your core business while we support you<br>with a dedicated cloud infrastructure.</li>
    <li style="top:2889px"><svg class="tick" viewBox="0 0 14 14"><circle cx="7" cy="7" r="7" fill="#1a8ed8"/><path d="M4 7.2l2 2 4-4" stroke="#fff" stroke-width="1.6" fill="none"/></svg>We’ll create and deliver the launchpad that will take your<br>business forward.</li>
  </ul>
  <div class="btn diff-btn">Learn More</div>
  <div class="diff-back abs"></div>
  <div class="diff-photo abs" role="img" aria-label="Hands typing on a laptop beneath glowing cloud network graphics"></div>
</section>

<!-- footer -->
<footer>
  <div class="footer abs"></div>
  <div class="brand abs" style="left:111px;top:3186px;font-size:33px"><span class="brand-dot" style="width:36px;height:36px"></span>Nuvexa Cloud</div>
  <div class="email abs">Enter Your Email<span class="email-send"><svg width="31" height="31" viewBox="0 0 31 31"><path d="M9 16l13-6-5 13-2-5z" fill="#fff"/></svg></span></div>
  <div class="social abs"><span></span><span></span><span></span><span></span></div>

  <div class="fcol">
    <h4 style="left:485px">Quick Link</h4>
    <a style="left:487px;top:3226px">Home</a>
    <a style="left:487px;top:3256px">About</a>
    <a style="left:487px;top:3286px">Product</a>
    <a style="left:487px;top:3316px">Solutions</a>
    <a style="left:487px;top:3346px">Contact Us</a>

    <h4 style="left:659px">Contact Us</h4>
    <svg class="contact-ico" style="left:662px;top:3229px" viewBox="0 0 14 14"><path d="M7 0a5 5 0 0 1 5 5c0 4-5 9-5 9S2 9 2 5a5 5 0 0 1 5-5z" fill="#fff"/><circle cx="7" cy="5" r="2" fill="#000"/></svg>
    <div style="left:687px;top:3226px;line-height:23px">Lorem ipsum dolor sit<br>amet, consectetur</div>
    <svg class="contact-ico" style="left:662px;top:3288px" viewBox="0 0 14 14"><rect y="2" width="14" height="10" fill="#fff"/><path d="M0 2l7 6 7-6" stroke="#000" fill="none"/></svg>
    <div style="left:687px;top:3285px">info@nuvexacloud.com</div>
    <svg class="contact-ico" style="left:662px;top:3322px" viewBox="0 0 14 14"><path d="M3 0l3 3-2 2c1 2 3 4 5 5l2-2 3 3-2 3C6 14 0 8 0 3z" fill="#fff"/></svg>
    <div style="left:687px;top:3319px">+1 555 014 2277</div>

    <h4 style="left:925px">Support</h4>
    <a style="left:927px;top:3226px">Terms&amp;condtions</a>
    <a style="left:927px;top:3256px">Privacy Policy</a>
    <a style="left:927px;top:3286px">About Us</a>
    <a style="left:927px;top:3316px">Support</a>
  </div>
  <div class="f-rule abs"></div>
  <div class="copyright abs">©Copyrights 2022 &nbsp;Nuvexa Cloud &nbsp;&nbsp;| &nbsp;&nbsp;All Rights Reserved</div>
</footer>

</body>
</html>
```